Wellness, weight management medical practice

We have a logo but want help designing and finalizing the business card. Japanese name. Will eventually be a holistic, full-service weight management and wellness center. Will be a virtual only practice to start.

```html
<!DOCTYPE html>
<html lang="en">
<head>
<meta charset="utf-8">
<title>Hoshiro Wellness – Business Card</title>
<link rel="stylesheet" href="https://fonts.googleapis.com/css2?family=Montserrat:wght@600;800&family=Open+Sans:wght@400;600&display=swap">
<style>
  :root {
    --backdrop: #242424;
    --card: #202024;
    --card-band-1: #1d1d21;
    --card-band-2: #1a1a1e;
    --card-band-3: #18181b;
    --gold: #e9bb2e;
    --gold-deep: #c98f16;
    --ink-light: #ffffff;
  }
  * { box-sizing: border-box; margin: 0; padding: 0; }
  html, body {
    width: 1200px; height: 780px; overflow: hidden;
    background: var(--backdrop);
  }
  .stage {
    position: relative; width: 1200px; height: 780px;
    display: flex; justify-content: center; align-items: center; gap: 80px;
  }
  .card {
    position: relative; width: 380px; height: 640px;
    background: var(--card); border-radius: 22px; overflow: hidden;
    box-shadow: 0 18px 40px rgba(0,0,0,.55);
  }
  .brand {
    position: absolute; left: 0; right: 0;
    display: flex; align-items: center; justify-content: center; gap: 10px;
    font-family: "Montserrat", sans-serif; font-weight: 600;
    color: var(--gold); letter-spacing: .06em;
  }
  .brand-dot {
    width: 12px; height: 12px; border-radius: 50%; background: var(--gold);
  }
  .card--front .brand { top: 300px; font-size: 28px; }
  .card--back .brand { top: 96px; font-size: 22px; }
  .card-bands { position: absolute; inset: 0; }
  .team {
    position: absolute; left: 0; right: 0; top: 318px; text-align: center;
  }
  .member-name {
    font-family: "Montserrat", sans-serif; font-weight: 800;
    color: var(--gold); font-size: 21px; line-height: 1.15;
  }
  .member-role {
    font-family: "Open Sans", sans-serif; font-weight: 600;
    color: var(--ink-light); font-size: 14px; margin-bottom: 12px;
  }
  .contact {
    position: absolute; left: 0; right: 0; top: 516px; text-align: center;
    font-family: "Open Sans", sans-serif; color: var(--ink-light);
  }
  .contact-icons { display: flex; justify-content: center; gap: 8px; margin-bottom: 8px; }
  .contact-icon {
    width: 26px; height: 26px; border-radius: 50%;
    background: linear-gradient(135deg, var(--gold), var(--gold-deep));
    display: flex; align-items: center; justify-content: center;
  }
  .contact-line { font-size: 16px; line-height: 1.4; }
</style>
</head>
<body>
<main class="stage">
  <section class="card card--front" aria-label="Card front">
    <div class="brand"><span class="brand-dot"></span><span>Hoshiro Wellness</span></div>
  </section>

  <section class="card card--back" aria-label="Card back">
    <svg class="card-bands" viewBox="0 0 380 640" width="380" height="640" aria-hidden="true">
      <defs>
        <filter id="band-shadow" x="-10%" y="-10%" width="120%" height="130%">
          <feDropShadow dx="0" dy="4" stdDeviation="5" flood-color="#000" flood-opacity=".45"/>
        </filter>
      </defs>
      <rect width="380" height="640" fill="var(--card-band-3)"/>
      <path d="M0 0 H380 V410 Q260 560 70 560 L0 560 Z" fill="var(--card-band-2)" filter="url(#band-shadow)"/>
      <path d="M0 0 H380 V380 Q280 500 60 500 L0 500 Z" fill="var(--card-band-1)" filter="url(#band-shadow)"/>
      <path d="M0 0 H380 V290 Q330 470 70 480 L0 480 Z" fill="var(--card)" filter="url(#band-shadow)"/>
    </svg>

    <div class="brand"><span class="brand-dot"></span><span>Hoshiro Wellness</span></div>

    <div class="team">
      <p class="member-name">Mara Linwood, NP</p>
      <p class="member-role">Co-Founder</p>
      <p class="member-name">Elliot Linwood, CRNA</p>
      <p class="member-role">Co-Founder</p>
    </div>

    <div class="contact">
      <div class="contact-icons">
        <span class="contact-icon" aria-label="Phone">
          <svg width="14" height="14" viewBox="0 0 24 24" aria-hidden="true"><path fill="#fff" d="M6.6 10.8a15.1 15.1 0 0 0 6.6 6.6l2.2-2.2a1 1 0 0 1 1-.25 11.4 11.4 0 0 0 3.6.57 1 1 0 0 1 1 1V20a1 1 0 0 1-1 1A17 17 0 0 1 3 4a1 1 0 0 1 1-1h3.5a1 1 0 0 1 1 1c0 1.25.2 2.45.57 3.6a1 1 0 0 1-.25 1z"/></svg>
        </span>
        <span class="contact-icon" aria-label="Email">
          <svg width="14" height="14" viewBox="0 0 24 24" aria-hidden="true"><path fill="#fff" d="M3 5h18a1 1 0 0 1 1 1v12a1 1 0 0 1-1 1H3a1 1 0 0 1-1-1V6a1 1 0 0 1 1-1zm9 7.2L4 7v1.8l8 5.2 8-5.2V7z"/></svg>
        </span>
      </div>
      <p class="contact-line">(555) 201-4478</p>
      <p class="contact-line">hoshirowellness@mail.com</p>
    </div>
  </section>
</main>
</body>
</html>
```